Oakhaven Construction Need an information and interactive website with client portal. We have ou

Need to have a client log in screen for work orders and estimate requests.
Nice informational landing page.

Oakhaven is a full service general contractor servicing apartment complexes;
maintenance of grounds and apartments - remodeling and construction.

Design Specifics: We are pretty open here. Some good examples are
www.marrowpeakbuilders.com , tovelresidence.com and www.quillbyworksite.com

For the site we need:
Homepage - to explain services
Roofing page
Apartment Page
Client Portal - where clients can set up accounts to set up work/estimate request that will be routed to our email

--Will need coding, plan to host site on Wordpress

Target Market(s)

Multi family, Residential and commercial clients

Industry/Entity Type

Construction

Coding

Coded - Design and coding required

Number of Pages Required

3 page

Font styles to use
Serif

Requirements
Must have
• Client portal
Nice to have
• Not sure. please advise

```html
<!DOCTYPE html>
<html lang="en">
<head>
<meta charset="utf-8">
<title>Oakhaven Construction</title>
<link rel="stylesheet" href="https://fonts.googleapis.com/css2?family=Roboto:wght@300;400;500;700&display=swap">
<style>
:root{
  --red:#e5262d;
  --red-soft:#ee4b4f;
  --ink:#222;
  --text:#555;
  --muted:#777;
  --line:#e6e6e6;
  --white:#fff;
  --foot-top:#2b2b2b;
  --foot-bottom:#050505;
  --foot-text:#d8d8d8;
  --hero-a:#5d4584;
  --hero-b:#8a5a8c;
}
*{box-sizing:border-box;margin:0;padding:0}
html,body{width:1200px;height:2500px;overflow:hidden;background:var(--white)}
body{font-family:'Roboto',Arial,sans-serif;color:var(--text);position:relative}
a{color:inherit;text-decoration:none}

/* header */
.site-header{height:122px;display:flex;align-items:center;justify-content:space-between;padding:0 98px 0 100px}
.brand{display:flex;align-items:center;gap:14px}
.brand-mark{width:38px;height:38px;background:var(--red)}
.brand-name{font-weight:700;font-size:26px;color:var(--ink);letter-spacing:1px;line-height:1}
.main-nav{display:flex;gap:36px;font-size:14px;color:var(--ink);text-transform:uppercase}
.main-nav a{padding:10px 0;position:relative}
.main-nav a.active{color:var(--red)}
.main-nav a.active::after{content:"";position:absolute;left:0;right:0;bottom:-6px;height:2px;background:var(--red)}

/* hero */
.hero{height:528px;position:relative;background:linear-gradient(180deg,var(--hero-a),var(--hero-b) 60%,#7a5560);text-align:center;color:var(--white)}
.hero-title{padding-top:178px;font-size:54px;font-weight:700;letter-spacing:.5px;text-shadow:0 2px 4px rgba(0,0,0,.35)}
.hero-sub{font-size:17px;line-height:26px;margin-top:6px;text-shadow:0 1px 2px rgba(0,0,0,.4)}
.hero-arrow{position:absolute;top:195px;width:46px;height:46px;border-radius:50%;background:rgba(255,255,255,.18);display:flex;align-items:center;justify-content:center}
.hero-arrow.prev{left:20px}.hero-arrow.next{right:20px}

/* welcome */
.welcome{height:545px;text-align:center;padding-top:40px}
.section-title{font-size:30px;font-weight:700;color:var(--ink);text-transform:uppercase}
.section-title span{color:var(--red)}
.welcome-intro{width:940px;margin:20px auto 0;font-size:14px;line-height:25px;color:var(--muted)}
.divider{width:1000px;height:1px;background:var(--line);margin:36px auto 0}
.services{display:flex;justify-content:center;margin-top:18px}
.service{width:258px;padding:0 14px}
.service-icon{width:140px;height:140px;margin:0 auto;border-radius:50%;background:var(--red);border:4px solid var(--white);box-shadow:0 0 0 3px var(--red);display:flex;align-items:center;justify-content:center}
.service-name{font-size:19px;color:var(--ink);margin-top:17px;text-transform:uppercase}
.service-text{font-size:13px;line-height:18px;color:var(--muted);margin-top:6px}
.btn-outline{display:inline-block;margin-top:18px;width:130px;height:36px;line-height:34px;border:1px solid var(--red);color:var(--red);font-size:14px;text-transform:uppercase}

/* about band */
.about-band{height:433px;background:linear-gradient(180deg,#ec5a5c,var(--red) 70%,#c92127);text-align:center;color:var(--white);padding-top:62px}
.about-title{font-size:44px;font-weight:400}
.about-text{width:980px;margin:22px auto 0;font-size:14px;line-height:26px}
.about-text p+p{margin-top:10px}
.btn-ghost{display:inline-block;margin-top:40px;width:220px;height:52px;line-height:50px;border:2px solid var(--white);border-radius:3px;font-size:19px;text-transform:uppercase}

/* gallery */
.gallery{display:flex;height:204px}
.gallery-tile{flex:1;display:flex;align-items:center;justify-content:center;color:var(--white);font-size:26px;text-transform:uppercase}
.tile-house{background:linear-gradient(180deg,#8cb0d8,#b53a32 55%,#4f7a2e)}
.tile-glass{background:linear-gradient(180deg,#3f7fbf,#2a5e95)}
.tile-office{background:linear-gradient(180deg,#b9cde0,#6d7e8f 60%,#88908a)}
.tile-frame{background:linear-gradient(180deg,#c8d8e6,#b08a5c 55%,#8b7d6a)}

/* clients */
.clients{height:338px;text-align:center;padding-top:40px}
.clients-intro{width:820px;margin:22px auto 0;font-size:13px;line-height:25px;color:var(--muted)}
.client-row{display:flex;align-items:center;justify-content:center;gap:24px;margin-top:50px;position:relative}
.client-logo{width:176px;height:88px;border:1px solid #d9d9d9;transform:skewX(-18deg);display:flex;align-items:center;justify-content:center}
.client-logo span{transform:skewX(18deg);font-size:19px;font-weight:700;color:var(--ink)}
.client-arrow{position:absolute;top:30px}
.client-arrow.prev{left:78px}.client-arrow.next{right:78px}

/* footer */
.site-footer{height:330px;background:linear-gradient(180deg,var(--foot-top),var(--foot-bottom));color:var(--foot-text);padding:48px 100px 0}
.footer-cols{display:flex;height:208px}
.footer-col{border-right:1px solid rgba(255,255,255,.06);padding-right:20px}
.footer-col:last-child{border-right:0}
.col-company{width:167px}.col-services{width:213px}.col-contact{width:288px}.col-why{width:174px}.col-follow{flex:1}
.footer-col + .footer-col{padding-left:0}
.footer-heading{font-size:16px;color:var(--white);text-transform:uppercase;margin-bottom:18px}
.footer-list{list-style:none;font-size:14px;line-height:30px}
.contact-line{display:flex;align-items:center;gap:10px;font-size:14px;line-height:30px}
.follow-text{font-size:14px}
.social{display:flex;gap:6px;margin-top:18px}
.social span{width:36px;height:36px;border-radius:50%;background:var(--red);border:2px solid var(--white)}
.footer-bottom{border-top:1px solid #555;padding-top:24px;font-size:13px;color:var(--white)}
</style>
</head>
<body>

<header class="site-header">
  <div class="brand">
    <span class="brand-mark"></span>
    <span class="brand-name">OAKHAVEN CONSTRUCTION</span>
  </div>
  <nav class="main-nav">
    <a class="active" href="#">Home</a>
    <a href="#">About Us</a>
    <a href="#">Roofing</a>
    <a href="#">Apartment</a>
    <a href="#">Client Portal</a>
    <a href="#">Contact Us</a>
  </nav>
</header>

<section class="hero" role="img" aria-label="Two-storey suburban house with garage and trees under a purple overlay">
  <h1 class="hero-title">OAKHAVEN CONSTRUCTIONS</h1>
  <p class="hero-sub">We are a general contracting company servicing apartment complexes, maintenance<br>of grounds and apartments - remodeling and construction.</p>
  <span class="hero-arrow prev"><svg width="14" height="24" viewBox="0 0 14 24"><path d="M12 2 2 12l10 10" fill="none" stroke="#fff" stroke-width="2"/></svg></span>
  <span class="hero-arrow next"><svg width="14" height="24" viewBox="0 0 14 24"><path d="M2 2l10 10L2 22" fill="none" stroke="#fff" stroke-width="2"/></svg></span>
</section>

<section class="welcome">
  <h2 class="section-title">Welcome to <span>Oakhaven Constructions</span></h2>
  <p class="welcome-intro">Sed ut perspiciatis unde omnis iste natus error sit voluptatem accusantium doloremque laudantium, totam rem aperiam, eaque ipsa quae ab illo inventore veritatis et quasi architecto beatae vitae dicta sunt explicabo.</p>
  <div class="divider"></div>
  <div class="services">
    <article class="service">
      <div class="service-icon"><svg width="60" height="60" viewBox="0 0 60 60" fill="#fff"><rect x="16" y="10" width="28" height="42"/><rect x="6" y="26" width="12" height="26"/><rect x="42" y="26" width="12" height="26"/><g fill="#e5262d"><rect x="21" y="15" width="6" height="6"/><rect x="33" y="15" width="6" height="6"/><rect x="21" y="26" width="6" height="6"/><rect x="33" y="26" width="6" height="6"/><rect x="26" y="40" width="8" height="12"/><rect x="9" y="31" width="5" height="5"/><rect x="46" y="31" width="5" height="5"/></g></svg></div>
      <h3 class="service-name">Apartments</h3>
      <p class="service-text">Sed ut perspiciatis unde omnis iste natus error sit voluptatem accusantium doloremque laudantium</p>
      <a class="btn-outline" href="#">Read More</a>
    </article>
    <article class="service">
      <div class="service-icon"><svg width="60" height="60" viewBox="0 0 60 60" fill="#fff"><path d="M30 8 52 50H8z"/><rect x="14" y="30" width="32" height="5" fill="#e5262d"/><rect x="4" y="50" width="52" height="5"/></svg></div>
      <h3 class="service-name">Construction</h3>
      <p class="service-text">Sed ut perspiciatis unde omnis iste natus error sit voluptatem accusantium doloremque laudantium</p>
      <a class="btn-outline" href="#">Read More</a>
    </article>
    <article class="service">
      <div class="service-icon"><svg width="64" height="64" viewBox="0 0 64 64"><g fill="#fff"><circle cx="32" cy="32" r="20"/><g stroke="#fff" stroke-width="9"><path d="M32 4v56M4 32h56M12 12l40 40M52 12 12 52"/></g></g><circle cx="32" cy="32" r="10" fill="#e5262d"/></svg></div>
      <h3 class="service-name">Maintenance</h3>
      <p class="service-text">Sed ut perspiciatis unde omnis iste natus error sit voluptatem accusantium doloremque laudantium</p>
      <a class="btn-outline" href="#">Read More</a>
    </article>
    <article class="service">
      <div class="service-icon"><svg width="60" height="60" viewBox="0 0 60 60" fill="#fff"><path d="M30 8 52 18 30 28 8 18z"/><path d="M8 22l20 9v21L8 43z"/><path d="M52 22 32 31v21l20-9z"/></svg></div>
      <h3 class="service-name">Remodeling</h3>
      <p class="service-text">Sed ut perspiciatis unde omnis iste natus error sit voluptatem accusantium doloremque laudantium</p>
      <a class="btn-outline" href="#">Read More</a>
    </article>
  </div>
</section>

<section class="about-band" role="img" aria-label="City skyline of high-rise towers under a red overlay">
  <h2 class="about-title">We are a General Contracting Company</h2>
  <div class="about-text">
    <p>We have a rapid response team for urgent needs and have relationship services that offer fixed pricing for most services and estimate pricing for larger and more complex solutions.</p>
    <p>But I must explain to you how all this mistaken idea of denouncing pleasure and praising pain was born and I will give you a complete account of the system, and expound the actual teachings of the great explorer of the truth, the master-builder of human happiness. No one rejects, dislikes, or avoids pleasure itself, because it is pleasure.</p>
  </div>
  <a class="btn-ghost" href="#">Read More</a>
</section>

<section class="gallery">
  <div class="gallery-tile tile-house" role="img" aria-label="Red cottage with a thatched roof"></div>
  <div class="gallery-tile tile-glass" role="img" aria-label="Glass facade being cleaned from a work platform">Construction</div>
  <div class="gallery-tile tile-office" role="img" aria-label="Modern office buildings along a tree-lined path"></div>
  <div class="gallery-tile tile-frame" role="img" aria-label="Timber-framed houses under construction"></div>
</section>

<section class="clients">
  <h2 class="section-title">Our <span>Clients</span></h2>
  <p class="clients-intro">At vero eos et accusamus et iusto odio dignissimos ducimus qui blanditiis praesentium voluptatum deleniti atque corrupti quos dolores et quas molestias excepturi sint occaecati cupiditate non provident.</p>
  <div class="client-row">
    <span class="client-arrow prev"><svg width="14" height="24" viewBox="0 0 14 24"><path d="M12 2 2 12l10 10" fill="none" stroke="#bbb" stroke-width="3"/></svg></span>
    <div class="client-logo"><span>Veltrix</span></div>
    <div class="client-logo"><span>Stonegate Builders</span></div>
    <div class="client-logo"><span>Brindle Construction</span></div>
    <div class="client-logo"><span>Stonegate Builders</span></div>
    <div class="client-logo"><span>Norvale</span></div>
    <span class="client-arrow next"><svg width="14" height="24" viewBox="0 0 14 24"><path d="M2 2l10 10L2 22" fill="none" stroke="#bbb" stroke-width="3"/></svg></span>
  </div>
</section>

<footer class="site-footer">
  <div class="footer-cols">
    <div class="footer-col col-company">
      <h4 class="footer-heading">Company</h4>
      <ul class="footer-list"><li>Home</li><li>About us</li><li>Roofing</li><li>Apartment</li><li>Contact us</li></ul>
    </div>
    <div class="footer-col col-services">
      <h4 class="footer-heading">Services</h4>
      <ul class="footer-list"><li>Appartments</li><li>Constructions</li><li>Maintenance</li><li>Remodeling</li></ul>
    </div>
    <div class="footer-col col-contact">
      <h4 class="footer-heading">Get in Touch</h4>
      <p class="contact-line"><svg width="14" height="14" viewBox="0 0 14 14"><path d="M3 1l2 3-1.5 1.5a8 8 0 0 0 5 5L10 9l3 2-1 2.5C6 14 0 8 .5 2z" fill="#fff"/></svg>Call us on 555-201-4837</p>
      <p class="contact-line"><svg width="14" height="11" viewBox="0 0 14 11"><rect width="14" height="11" fill="#fff"/><path d="M0 0l7 6 7-6" fill="none" stroke="#222" stroke-width="1.4"/></svg>info@oakhavenbuild.com</p>
    </div>
    <div class="footer-col col-why">
      <h4 class="footer-heading">Why Us</h4>
      <ul class="footer-list"><li>My Account</li><li>Team</li><li>Privacy &amp; Policy</li><li>FAQ</li></ul>
    </div>
    <div class="footer-col col-follow">
      <h4 class="footer-heading">Follow Us</h4>
      <p class="follow-text">Please connect with us on</p>
      <div class="social" aria-label="Social profiles"><span></span><span></span><span></span><span></span></div>
    </div>
  </div>
  <div class="footer-bottom">© 2016 Company Name&nbsp; All right reserved&nbsp; Term of Use</div>
</footer>

</body>
</html>
```